Kettle Moor Gluten Free Bread Packaging Design

We need a new packaging design for Kettle Moor Gluten Free bread company. The company currently produces gluten free bread, cinnamon roll, bagels, shortbread and other pastries.
We need a new packaging design for our packaging. You can see more about the company at http://kettlemoorgf.com/. Please incorporate the existing logo into the overall packaging design.
Here are some of the inspiration we would like used for a new design:
1. http://www.plinthsketchy.com/2016/02/23/10-stunning-product-packaging-label-designs-for-your-inspiration/ (# 1 and 5 only)
2. http://www.plinthsketchy.com/wp-content/uploads/2015/05/Simple-Yet-Modern-Packaging-Designs-Product-Photography-Examples-for-Inspiration-37.jpg
3. http://www.plinthsketchy.com/wp-content/uploads/2015/05/Simple-Yet-Modern-Packaging-Designs-Product-Photography-Examples-for-Inspiration-18.jpg
4. http://www.plinthsketchy.com/wp-content/uploads/2015/05/Simple-Yet-Modern-Packaging-Designs-Product-Photography-Examples-for-Inspiration-11.jpg
5. http://crandlevo.org/2016/08/02/branding-pale-thistle-company/ (could do black label with blue and gold outline of existing logo)
6. http://crandlevo.org/2016/04/21/packaging-ironwick-roasters
Target Market(s)
The target market is the health conscious consumer that is willing to pay a premium for gluten free and vegan options.
Industry/Entity Type
It Company
Look and feel

```html
<!DOCTYPE html>
<html lang="en">
<head>
<meta charset="utf-8">
<title>Kettle Moor Gluten Free — Packaging Range</title>
<link href="https://fonts.googleapis.com/css2?family=Titillium+Web:wght@300;400;700&display=swap" rel="stylesheet">
<style>
  :root {
    --page-bg: #ffffff;
    --label-white: #ffffff;
    --brand-teal: #1aa6b0;
    --ink-black: #000000;
    --glow-grey: #4b4e54;
    --title-white: #ffffff;
    --cinnamon: #d9955e;
    --cinnamon-text: #e0a477;
    --buns: #7fb0c9;
    --buns-text: #8fbad0;
    --bread: #c8ac72;
    --bread-text: #d1b886;
    --bagels: #a9c47f;
    --bagels-text: #b5cd90;
    --shortbread: #d8776b;
    --shortbread-text: #df8a7f;
  }
  * { box-sizing: border-box; margin: 0; padding: 0; }
  html, body {
    width: 1200px; height: 552px; overflow: hidden;
    background: var(--page-bg);
    font-family: "Titillium Web", sans-serif;
  }
  .range { position: relative; width: 1200px; height: 552px; }
  .pack {
    position: absolute; top: 64px; width: 231px; height: 416px;
    --accent: var(--cinnamon); --accent-text: var(--cinnamon-text);
  }
  .pack--cinnamon { left: 7px; }
  .pack--buns { left: 246px; --accent: var(--buns); --accent-text: var(--buns-text); }
  .pack--bread { left: 484px; --accent: var(--bread); --accent-text: var(--bread-text); }
  .pack--bagels { left: 722px; --accent: var(--bagels); --accent-text: var(--bagels-text); }
  .pack--shortbread { left: 961px; --accent: var(--shortbread); --accent-text: var(--shortbread-text); }

  .pack__pattern {
    position: absolute; left: 0; top: 0; width: 100%; height: 123px;
    background: var(--accent);
  }
  .pack__body {
    position: absolute; left: 0; top: 125px; width: 100%; bottom: 0;
    background: radial-gradient(ellipse 120px 95px at 60% 22%, var(--glow-grey) 0%, #1d1f22 60%, var(--ink-black) 100%);
  }
  .pack__label {
    position: absolute; left: 49px; top: 0; width: 130px; height: 221px;
    background: var(--label-white);
    box-shadow: 3px 3px 4px rgba(0,0,0,0.55);
    display: flex; align-items: center; justify-content: center;
  }
  .brand {
    color: var(--brand-teal); font-weight: 700; font-size: 28px;
    line-height: 1.05; text-transform: uppercase; text-align: center;
  }
  .pack__claim {
    position: absolute; left: 0; width: 100%; top: 316px;
    text-align: center; color: var(--accent-text);
    font-size: 12px; line-height: 15px; font-weight: 400; text-transform: uppercase;
  }
  .pack__rule {
    position: absolute; left: 12px; width: 208px; height: 1px;
    background: var(--accent);
  }
  .pack__rule--top { top: 332px; }
  .pack__rule--bottom { top: 385px; }
  .pack__product {
    position: absolute; left: 0; width: 100%; top: 333px;
    text-align: center; color: var(--title-white);
    font-weight: 300; font-size: 44px; line-height: 52px;
    text-transform: uppercase; white-space: nowrap;
  }
  .pack--cinnamon .pack__product { font-size: 27px; }
  .pack--shortbread .pack__product { font-size: 31px; }
</style>
</head>
<body>
<main class="range">
  <section class="pack pack--cinnamon">
    <div class="pack__pattern" role="img" aria-label="Hand-drawn bakery pattern of croissants, whisks and pastries in orange"></div>
    <div class="pack__body"></div>
    <div class="pack__label"><p class="brand">Kettle<br>Moor</p></div>
    <p class="pack__claim">Gluten free &amp; vegan</p>
    <span class="pack__rule pack__rule--top"></span>
    <h2 class="pack__product">Cinnamon Roll</h2>
    <span class="pack__rule pack__rule--bottom"></span>
  </section>
  <section class="pack pack--buns">
    <div class="pack__pattern" role="img" aria-label="Hand-drawn bakery pattern of croissants, whisks and pastries in blue"></div>
    <div class="pack__body"></div>
    <div class="pack__label"><p class="brand">Kettle<br>Moor</p></div>
    <p class="pack__claim">Gluten free &amp; vegan</p>
    <span class="pack__rule pack__rule--top"></span>
    <h2 class="pack__product">Buns</h2>
    <span class="pack__rule pack__rule--bottom"></span>
  </section>
  <section class="pack pack--bread">
    <div class="pack__pattern" role="img" aria-label="Hand-drawn bakery pattern of croissants, whisks and pastries in tan"></div>
    <div class="pack__body"></div>
    <div class="pack__label"><p class="brand">Kettle<br>Moor</p></div>
    <p class="pack__claim">Gluten free &amp; vegan</p>
    <span class="pack__rule pack__rule--top"></span>
    <h2 class="pack__product">Bread</h2>
    <span class="pack__rule pack__rule--bottom"></span>
  </section>
  <section class="pack pack--bagels">
    <div class="pack__pattern" role="img" aria-label="Hand-drawn bakery pattern of croissants, whisks and pastries in green"></div>
    <div class="pack__body"></div>
    <div class="pack__label"><p class="brand">Kettle<br>Moor</p></div>
    <p class="pack__claim">Gluten free &amp; vegan</p>
    <span class="pack__rule pack__rule--top"></span>
    <h2 class="pack__product">Bagels</h2>
    <span class="pack__rule pack__rule--bottom"></span>
  </section>
  <section class="pack pack--shortbread">
    <div class="pack__pattern" role="img" aria-label="Hand-drawn bakery pattern of croissants, whisks and pastries in coral red"></div>
    <div class="pack__body"></div>
    <div class="pack__label"><p class="brand">Kettle<br>Moor</p></div>
    <p class="pack__claim">Gluten free &amp; vegan</p>
    <span class="pack__rule pack__rule--top"></span>
    <h2 class="pack__product">Short Bread</h2>
    <span class="pack__rule pack__rule--bottom"></span>
  </section>
</main>
</body>
</html>
```